Business Card for a Candle Company. - Creative Hipster Styling :)

I am after a two sided Business Card. Contact information on the front, text that will be supplied (and details further on here) on the back. Ideally I am looking for someone I can continue to work with in the future for flyers, labels, marketing material etc.

I have a Logo which I am using as the labels for the candle and have attached all the versions of the file I was given. I am after a similar feel to my logo and love the font and the feather used. it is important that my card looks like it is meant to go with the logo.

I would love you to use your imagination and see what can be thought up :)

All my candles are either clear or black glass and packaging is black and labels are white, on a square label with black writing (see attachments)

I love the feather on the logo if it can be incorporated great, if the business card looks better without it than that is fine too..

Target Market(s)

I am a new candle company and the feel I'm going for is a little luxury a little hipster. Imagine the candle going into a converted warehouse studio in the city.

Industry/Entity Type

Home And Garden

Contact Information for Business Card

I have a Logo which I am using as the labels for the candle and have attached all the versions of the file I was given. I am after a similar feel to my logo and love the font used but its caps and I don't really want everything in CAPS. It is important thought that everything goes together.

I love the feather on the logo if it can be incorporated great, if the business card looks better without it than that is fine too.

Morrel Wick Co
Central Coast, NSW Australia
A little wax company, in a garage, on the coast.
craftlane.example/au/shop/MorrelWickCo
friendspace.example.au/morrelwickco
morrelwickco@mailbox.example.au
Jess Holloran
0481 572 316.

On the back of the card I need it to look good and go with the design on the front but want a bit of text;

To give you an idea of what I want on the back I've put what I've got following but I'm still working on grammar and wording so it may change slightly before the final edit.

We would love to see how you display your candle or reuse the glass vessel and would love to see a photo!
Check out ideas and share yours on your social media #morrelwickco

Just a few ideas to reuse your vessel;

A Vase to Display fresh flowers
Lolly Jar for your favourite candy
Decorate with baubles at Christmas
Bathroom Vanity Storage
Decorate with eggs at Easter
Plant a teranium inside.

Font styles to use
Decorative
Script
Other font styles liked:
• OctinVintageFree

Colors
000000
ffffff
757575

Requirements
Must have
• The only must is that it needs to look like it goes with my logo which I am using as the labels on the actual candle. the labels are white with black details and are square.
• Not too structured if possible as it is a creative company rather that a professional services company.
• I want people to pick up the card and think it looks great. I believe a business card is a very useful marketing tool and should be used as such. One card will be included in with each candle so that customers can re order.
Nice to have
• I love the feather on the logo if it can be incorporated great, if the business card looks better without it than that is fine too.
• Card just needs to fit with the logo.
Should not have
• It should not be a boring card. :)

```html
<!DOCTYPE html>
<html lang="en">
<head>
<meta charset="utf-8">
<title>Morrel Wick Co – Business Card</title>
<link href="https://fonts.googleapis.com/css2?family=Roboto+Slab:wght@400&family=Open+Sans:wght@400&display=swap" rel="stylesheet">
<style>
  :root {
    --backdrop: #3a332e;
    --card: #050505;
    --card-edge: #1a1a1a;
    --ink: #ffffff;
    --ink-soft: #d9d9d9;
    --grey: #757575;
    --copper: #9a6a45;
  }
  * { box-sizing: border-box; margin: 0; padding: 0; }
  html, body { width: 1200px; height: 900px; overflow: hidden; }
  body {
    background: var(--backdrop);
    font-family: "Open Sans", sans-serif;
    position: relative;
  }
  .card {
    position: absolute;
    top: 300px;
    width: 540px;
    height: 310px;
    background: var(--card);
    border: 1px solid var(--card-edge);
    box-shadow: 0 12px 30px rgba(0,0,0,.45);
  }
  .card--front { left: 40px; }
  .card--back { left: 620px; }

  .brand {
    position: absolute;
    left: 36px;
    top: 104px;
    width: 210px;
    text-align: center;
  }
  .brand__name {
    font-family: "Roboto Slab", serif;
    font-size: 24px;
    letter-spacing: 1px;
    color: var(--ink);
    white-space: nowrap;
  }
  .brand__art {
    display: block;
    margin: 14px auto 0;
    width: 120px;
    height: 38px;
    border-radius: 50%;
    background: linear-gradient(90deg, #2a1d14, var(--copper), #2a1d14);
    opacity: .8;
  }
  .card--back .brand__art {
    background: linear-gradient(90deg, #2b2b2b, var(--grey), #2b2b2b);
  }

  .contact {
    position: absolute;
    left: 262px;
    top: 112px;
    list-style: none;
  }
  .contact li {
    display: flex;
    align-items: center;
    gap: 10px;
    font-size: 12.5px;
    line-height: 22px;
    color: var(--ink);
    white-space: nowrap;
  }
  .contact svg { width: 12px; height: 12px; flex: none; }

  .ideas {
    position: absolute;
    left: 270px;
    top: 64px;
    list-style: none;
  }
  .ideas li {
    display: flex;
    align-items: center;
    gap: 10px;
    font-size: 12.5px;
    line-height: 26px;
    color: var(--ink-soft);
    white-space: nowrap;
  }
  .ideas li::before {
    content: "";
    width: 8px;
    height: 8px;
    border-radius: 50%;
    background: var(--ink-soft);
    flex: none;
  }
</style>
</head>
<body>

<section class="card card--front" aria-label="Card front">
  <div class="brand">
    <div class="brand__name">Morrel Wick Co</div>
    <span class="brand__art" role="img" aria-label="Brand feather illustration area"></span>
  </div>
  <ul class="contact">
    <li>
      <svg viewBox="0 0 12 12" aria-hidden="true"><path d="M2.5 1h2l1 2.6-1.3 1a6 6 0 0 0 3.2 3.2l1-1.3L11 7.5v2a1.5 1.5 0 0 1-1.6 1.5A9 9 0 0 1 1 2.6 1.5 1.5 0 0 1 2.5 1z" fill="#9a6a45"/></svg>
      0481 572 316
    </li>
    <li>
      <svg viewBox="0 0 12 12" aria-hidden="true"><rect x="0.5" y="2" width="11" height="8" fill="#9a6a45"/><path d="M0.5 2l5.5 4.5L11.5 2" fill="none" stroke="#050505" stroke-width="1"/></svg>
      morrelwickco@mailbox.example.au
    </li>
    <li>
      <svg viewBox="0 0 12 12" aria-hidden="true"><rect x="1" y="1" width="10" height="10" fill="#9a6a45"/></svg>
      craftlane.example/au/shop/MorrelWickCo
    </li>
    <li>
      <svg viewBox="0 0 12 12" aria-hidden="true"><rect x="1" y="1" width="10" height="10" fill="#9a6a45"/></svg>
      friendspace.example.au/morrelwickco
    </li>
  </ul>
</section>

<section class="card card--back" aria-label="Card back">
  <div class="brand">
    <div class="brand__name">Morrel Wick Co</div>
    <span class="brand__art" role="img" aria-label="Brand feather illustration area"></span>
  </div>
  <ul class="ideas">
    <li>A Vase to Display fresh flowers</li>
    <li>Lolly Jar for your favourite candy</li>
    <li>Decorate with baubles at Christmas</li>
    <li>Bathroom Vanity Storage</li>
    <li>Decorate with eggs at Easter</li>
    <li>Plant a teranium inside.</li>
  </ul>
</section>

</body>
</html>
```